Business Card Design Project

- makeup artist business card

- original and creative

- Elegant design

- Feel free to come out with cool designs but stick to being elegant and attractive

- Design relates to makeup

- includes name, occupation, contact numbers, email, website

- regular size business card

- round corner card

- double sided

- on 1 side it should just have the website name in the center " browsandblush.example "

Industry/Entity Type

Business

Requirements
Must have
• Marla Voss
Makeup Artist
USA: +1 (415)872-6410
Singapore: +65 83027715
marlavoss@browsandblush.example
www.browsandblush.example
Should not have
• nothing cartoon looking.
Pictures of makeup being grab from the internet.. Examples: eyes or lips.

```html
<!DOCTYPE html>
<html lang="en">
<head>
<meta charset="utf-8">
<title>Marla Voss – Makeup Artist Business Card</title>
<link rel="stylesheet" href="https://fonts.googleapis.com/css2?family=Tinos:wght@400;700&display=swap">
<style>
  :root {
    --page-bg: #e9e9eb;
    --card-light: #fbfbfb;
    --card-shade: #dcdcdc;
    --frame-white: #f4f4f4;
    --ink: #111111;
    --accent-red: #d8232a;
    --band-text: #ffffff;
    --skin-light: #e9b79c;
    --skin-mid: #c98f76;
    --lash-dark: #1c1a1a;
    --shadow: rgba(0, 0, 0, 0.28);
  }
  * { box-sizing: border-box; margin: 0; padding: 0; }
  html, body { width: 1067px; height: 1200px; overflow: hidden; }
  body {
    background: var(--page-bg);
    font-family: "Tinos", "Times New Roman", serif;
    position: relative;
  }
  .card {
    position: absolute;
    left: 143px;
    width: 780px;
    height: 430px;
    border-radius: 26px;
    overflow: hidden;
    box-shadow: 0 10px 28px var(--shadow);
  }
  .card--front {
    top: 110px;
    background: radial-gradient(ellipse at 65% 40%, var(--card-light) 0%, #f0f0f0 55%, var(--card-shade) 100%);
  }
  .card--back {
    top: 660px;
    background: linear-gradient(160deg, #6d5048 0%, var(--lash-dark) 35%, #3a302e 60%, var(--skin-mid) 100%);
  }
  .portrait-frame {
    position: absolute;
    left: 16px;
    top: 16px;
    width: 352px;
    height: 398px;
    background: var(--frame-white);
    border-radius: 14px;
    box-shadow: 2px 3px 8px rgba(0,0,0,0.18);
    padding: 12px 12px 18px 12px;
  }
  .portrait {
    width: 100%;
    height: 100%;
    background: linear-gradient(180deg, var(--skin-light) 0%, #8a6a60 30%, var(--lash-dark) 48%, #9c8f88 62%, var(--skin-light) 100%);
  }
  .identity {
    position: absolute;
    left: 400px;
    top: 52px;
    width: 340px;
    text-align: center;
  }
  .identity__name {
    font-size: 40px;
    font-weight: 700;
    color: var(--ink);
    line-height: 1;
  }
  .identity__surname { color: var(--accent-red); }
  .identity__role {
    font-size: 22px;
    color: var(--ink);
    margin-top: 4px;
    padding-left: 110px;
  }
  .contact-bands {
    position: absolute;
    left: 368px;
    top: 208px;
    width: 398px;
    list-style: none;
  }
  .contact-bands li {
    background: var(--accent-red);
    color: var(--band-text);
    font-size: 21px;
    height: 31px;
    line-height: 31px;
    padding-left: 8px;
    margin-bottom: 3px;
    white-space: nowrap;
  }
  .back-photo {
    position: absolute;
    inset: 0;
  }
  .back-url {
    position: absolute;
    top: 72px;
    left: 0;
    width: 100%;
    text-align: center;
    color: #ffffff;
    font-size: 46px;
    letter-spacing: 0.5px;
  }
</style>
</head>
<body>
  <section class="card card--front" aria-label="Business card front">
    <div class="portrait-frame">
      <div class="portrait" role="img" aria-label="Close-up photograph of a made-up eye with dark smoky liner"></div>
    </div>
    <div class="identity">
      <h1 class="identity__name">Marla <span class="identity__surname">Voss</span></h1>
      <p class="identity__role">Makeup Artist</p>
    </div>
    <ul class="contact-bands">
      <li>Phone USA: +1 (415)872-6410</li>
      <li>Phone Singapore: +65 83027715</li>
      <li>marlavoss@browsandblush.example</li>
      <li>www.browsandblush.example</li>
    </ul>
  </section>

  <section class="card card--back" aria-label="Business card back">
    <div class="back-photo" role="img" aria-label="Full-bleed photograph of a made-up eye with dark smoky shadow and long lashes"></div>
    <p class="back-url">www.browsandblush.example</p>
  </section>
</body>
</html>
```